New look while maintaining the Brand identification!

I want a new look for my business card. I want to keep the same colors and feel but change the look and layout a bit. The logo (KALMORETIX Physical therapy Reimagined and the lilypad) must remain the same and in that font.
We are a physical therapy clinic. So we have certification that we can write on the back or services we provide (which is what we currently have on the back of the card as well)

Contact information
2840 Cedar Hollow Rd., #22
Naples, FL 34276
P: (239) 555-0172
F: (239) 555-0198
E: kalmoretixcare@mailvexo.com
W: www.kalmoretixcare-example.com

Industry/Entity Type

Physical Therapy

Contact Information for Business Card

Our current cards have the business address and information on the back. But I am willing to have it be in the front.

Font styles to use
Sans Serif

Colors
abd036
fbf289
ec1f27

Requirements
Must have
• Has to be unique!
• Services we provide and/or techniques we do must fit on the card
Nice to have
• Would like to have the front and back somehow linked together. Such that if you set the front next to the back, there is a nice flow of design! Currently the back is white with writing on it.
Should not have
• I like the wave lines as compared to straight lines.

```html
<!DOCTYPE html>
<html lang="en">
<head>
<meta charset="utf-8">
<title>Kalmoretix Business Card</title>
<link href="https://fonts.googleapis.com/css2?family=Source+Sans+3:wght@400;600&display=swap" rel="stylesheet">
<style>
  :root {
    --backdrop: #3a3a3a;
    --card: #f8f8f7;
    --gold: #cdb000;
    --leaf: #8a9a1e;
    --ink: #454545;
    --white: #ffffff;
  }
  html, body {
    margin: 0;
    width: 1200px;
    height: 750px;
    overflow: hidden;
    background: var(--backdrop);
    font-family: "Source Sans 3", sans-serif;
  }
  .canvas { position: relative; width: 1200px; height: 750px; }
  .card {
    position: absolute;
    top: 228px;
    width: 461px;
    height: 262px;
    border-radius: 14px;
    background: var(--card);
    overflow: hidden;
  }
  .card-front { left: 124px; }
  .card-back { left: 618px; }
  .wave { position: absolute; inset: 0; }
  .person {
    position: absolute;
    right: 24px;
    top: 16px;
    text-align: right;
    color: var(--white);
  }
  .person-name { font-size: 18px; font-weight: 600; letter-spacing: 0.3px; line-height: 1; }
  .person-role { font-size: 13.5px; margin-top: 4px; }
  .brand-name {
    position: absolute;
    left: 24px;
    top: 103px;
    font-size: 40px;
    font-weight: 600;
    color: var(--gold);
    letter-spacing: 0.5px;
    line-height: 1;
  }
  .contact-list {
    position: absolute;
    left: 25px;
    top: 172px;
    margin: 0;
    padding: 0;
    list-style: none;
    color: var(--ink);
    font-size: 13px;
  }
  .contact-list li { display: flex; align-items: center; height: 17.6px; }
  .contact-list svg { width: 12px; height: 12px; margin-right: 6px; fill: var(--gold); }
  .address {
    position: absolute;
    right: 24px;
    top: 207px;
    text-align: right;
    color: var(--ink);
    font-size: 13px;
    line-height: 17.6px;
    font-style: normal;
  }
</style>
</head>
<body>
<main class="canvas">
  <section class="card card-front">
    <svg class="wave" viewBox="0 0 461 262" aria-hidden="true">
      <path d="M0,0 H461 V160 C380,92 250,20 120,22 C60,24 20,36 0,44 Z" fill="var(--gold)"/>
      <path d="M0,50 C40,37 100,30 150,32 C260,37 380,102 461,172 V188 C380,122 260,52 150,43 C90,40 40,46 0,56 Z" fill="var(--leaf)"/>
    </svg>
    <div class="person">
      <div class="person-name">DANIEL MARSH</div>
      <div class="person-role">CEO/Founder</div>
    </div>
    <div class="brand-name">KALMORETIX</div>
    <ul class="contact-list">
      <li><svg viewBox="0 0 12 12"><path d="M2.5,0.5 L4.5,0.5 L5.3,3.3 L4,4.4 C4.7,6 6,7.3 7.6,8 L8.7,6.7 L11.5,7.5 L11.5,9.5 C11.5,10.6 10.6,11.5 9.5,11.5 C4.5,11.2 0.8,7.5 0.5,2.5 C0.5,1.4 1.4,0.5 2.5,0.5 Z"/></svg>(239) 555-0172</li>
      <li><svg viewBox="0 0 12 12"><rect x="3" y="0.5" width="6" height="3.5"/><rect x="0.5" y="4.5" width="11" height="5" rx="1"/><rect x="2.5" y="8.5" width="7" height="3"/></svg>(239) 555-0198</li>
      <li><svg viewBox="0 0 12 12"><path d="M0.5,2.5 H11.5 V9.5 H0.5 Z M1.5,3.2 L6,6.6 L10.5,3.2" stroke="var(--white)" stroke-width="0.8"/></svg>kalmoretixcare@mailvexo.com</li>
      <li><svg viewBox="0 0 12 12"><circle cx="6" cy="6" r="5.5"/><path d="M6,0.5 V11.5 M0.5,6 H11.5 M6,0.5 C3,3 3,9 6,11.5 M6,0.5 C9,3 9,9 6,11.5" stroke="var(--white)" stroke-width="0.6" fill="none"/></svg>www.kalmoretixcare-example.com</li>
    </ul>
    <address class="address">2840 Cedar Hollow Rd., #22<br>Naples, FL 34276</address>
  </section>
  <section class="card card-back"></section>
</main>
</body>
</html>
```